Yard Sign Design Needed

Yard sign needed for mowing & landscaping company. Would like to use the top logo with black background which is attached. Would like MOWING to be in large standout letters. The word "landscaping" can be smaller and more artistic or omitted. Will need room for phone number once design is approved. The phone number will need to stand out and look identical/similar to the word 'MOWING"

```html
<!DOCTYPE html>
<html lang="en">
<head>
<meta charset="utf-8">
<title>Talven Contractors – Mowing Yard Sign</title>
<link href="https://fonts.googleapis.com/css2?family=Exo+2:wght@600&family=Montserrat:wght@900&family=Permanent+Marker&display=swap" rel="stylesheet">
<style>
  :root {
    --sign-black: #000000;
    --lawn-green: #8a9c18;
    --paper-white: #ffffff;
  }
  * { margin: 0; padding: 0; box-sizing: border-box; }
  html, body {
    width: 1200px;
    height: 900px;
    overflow: hidden;
    background: var(--sign-black);
  }
  .yard-sign {
    position: relative;
    width: 1200px;
    height: 900px;
    background: var(--sign-black);
    overflow: hidden;
  }
  .brand-mark {
    position: absolute;
    left: 222px;
    top: 118px;
    width: 160px;
    height: 160px;
    background: var(--lawn-green);
  }
  .brand-name {
    position: absolute;
    left: 470px;
    top: 96px;
    width: 520px;
    font-family: "Exo 2", sans-serif;
    font-weight: 600;
    line-height: 1;
    text-align: center;
  }
  .brand-name__primary {
    display: block;
    font-size: 104px;
    letter-spacing: 16px;
    margin-right: -16px;
    color: var(--lawn-green);
  }
  .brand-name__secondary {
    display: block;
    font-size: 50px;
    letter-spacing: 6px;
    margin-right: -6px;
    margin-top: 2px;
    color: var(--paper-white);
  }
  .brand-name__suffix {
    display: flex;
    align-items: center;
    gap: 18px;
    font-size: 26px;
    letter-spacing: 4px;
    margin-top: 8px;
    color: var(--paper-white);
  }
  .brand-name__suffix::before,
  .brand-name__suffix::after {
    content: "";
    flex: 1;
    height: 2px;
    background: var(--paper-white);
  }
  .service-main {
    position: absolute;
    left: 0;
    width: 100%;
    top: 374px;
    text-align: center;
    font-family: "Montserrat", sans-serif;
    font-weight: 900;
    font-size: 188px;
    line-height: 1;
    color: var(--lawn-green);
    letter-spacing: 2px;
  }
  .lawn-band {
    position: absolute;
    left: 0;
    right: 0;
    top: 620px;
    bottom: 0;
    background: linear-gradient(to bottom, rgba(138,156,24,0) 0px, var(--lawn-green) 124px, var(--lawn-green) 100%);
  }
  .service-secondary {
    position: absolute;
    left: 0;
    width: 100%;
    top: 566px;
    text-align: center;
    font-family: "Permanent Marker", cursive;
    font-weight: 400;
    font-size: 100px;
    line-height: 1;
    color: var(--paper-white);
    z-index: 2;
  }
  .phone-number {
    position: absolute;
    left: 0;
    width: 100%;
    top: 767px;
    text-align: center;
    font-family: "Montserrat", sans-serif;
    font-weight: 900;
    font-size: 112px;
    line-height: 1;
    color: var(--paper-white);
    letter-spacing: 4px;
    word-spacing: 12px;
  }
</style>
</head>
<body>
  <main class="yard-sign">
    <div class="brand-mark" aria-hidden="true"></div>
    <div class="brand-name">
      <span class="brand-name__primary">TALVEN</span>
      <span class="brand-name__secondary">CONTRACTORS</span>
      <span class="brand-name__suffix">LLC</span>
    </div>

    <h1 class="service-main">MOWING</h1>

    <div class="lawn-band" role="img" aria-label="Green grass silhouette along the bottom of the sign"></div>

    <h2 class="service-secondary">LANDSCAPING</h2>

    <p class="phone-number">555 0148 2736</p>
  </main>
</body>
</html>
```